Structural Engineering Business Card

Veltrow Drafts does residential house plans for clients in Central Florida. Would like simple but elegant business card that is appropriate for a house plan engineering company. Prefer black business card with black/white them but open to other shades of blue. I uploaded a sample card that I came across that looked good but please come up with your own creative designs.

Contact Information for Business Card

Name, Title, Phone, Email, Address, website

```html
<!DOCTYPE html>
<html lang="en">
<head>
<meta charset="UTF-8">
<title>Veltrow Drafts — Business Card</title>
<link href="https://fonts.googleapis.com/css2?family=Jost:wght@400;600;700&display=swap" rel="stylesheet">
<style>
  :root {
    --page: #ffffff;
    --card: #000000;
    --ink: #ffffff;
    --line-soft: #c4c4c4;
    --plan-light: #4a4a4a;
    --plan-mid: #2a2a2a;
    --grid-tone: #1a1616;
  }
  * { margin: 0; padding: 0; box-sizing: border-box; }
  html, body { width: 1200px; height: 1200px; overflow: hidden; background: var(--page); }
  body { position: relative; font-family: 'Jost', sans-serif; color: var(--ink); }

  .card {
    position: absolute;
    top: 458px;
    width: 497px;
    height: 283px;
    background: var(--card);
    overflow: hidden;
  }
  .card--front { left: 76px; }
  .card--back { left: 626px; }

  .brand-name {
    font-weight: 700;
    letter-spacing: 0.02em;
    text-transform: uppercase;
    white-space: nowrap;
    display: flex;
    align-items: center;
  }
  .brand-mark {
    display: inline-block;
    background: var(--ink);
    margin-right: 8px;
  }

  .card--front .brand-name { position: absolute; left: 52px; top: 46px; font-size: 21px; z-index: 1; }
  .card--front .brand-mark { width: 13px; height: 13px; }

  .person { position: absolute; left: 52px; top: 105px; z-index: 1; }
  .person__name { font-weight: 600; font-size: 15px; line-height: 1.45; }
  .person__title { font-weight: 400; font-size: 15px; line-height: 1.3; }

  .contact-list { position: absolute; left: 52px; top: 162px; list-style: none; z-index: 1; }
  .contact-list li { display: flex; align-items: center; font-size: 13.5px; height: 24px; }
  .contact-list svg { width: 15px; height: 15px; margin-right: 9px; flex: none; }

  .address { position: absolute; left: 52px; top: 246px; font-size: 14px; z-index: 1; }

  .plan-art {
    position: absolute;
    right: 0; top: 0;
    width: 200px; height: 283px;
    background:
      radial-gradient(ellipse at 70% 40%, var(--plan-light) 0%, var(--plan-mid) 45%, rgba(0,0,0,0) 80%),
      linear-gradient(135deg, rgba(0,0,0,0) 20%, var(--plan-mid) 60%, #111 100%);
    clip-path: polygon(62% 0, 100% 0, 100% 100%, 12% 100%, 0 70%, 30% 30%);
  }

  .card--back .grid-fill {
    position: absolute; inset: 0;
    background: radial-gradient(ellipse at 50% 50%, var(--grid-tone) 0%, #0b0909 70%, var(--card) 100%);
  }
  .card--back .frame { position: absolute; inset: 0; width: 100%; height: 100%; }
  .card--back .brand-name {
    position: absolute; left: 0; right: 0; top: 100px;
    justify-content: center; font-size: 30px;
  }
  .card--back .brand-mark { width: 18px; height: 18px; margin-right: 11px; }
  .card--back .website {
    position: absolute; left: 0; right: 0; top: 198px;
    text-align: center; font-size: 26px; font-weight: 400; letter-spacing: 0.01em;
  }
</style>
</head>
<body>

  <section class="card card--front">
    <div class="plan-art" role="img" aria-label="Architectural floor plan drawing in white line work"></div>

    <div class="brand-name"><span class="brand-mark"></span>Veltrow Drafts</div>

    <div class="person">
      <p class="person__name">Dana Morrow</p>
      <p class="person__title">Manager</p>
    </div>

    <ul class="contact-list">
      <li>
        <svg viewBox="0 0 16 16" fill="none" stroke="#fff" stroke-width="1.3"><rect x="1.5" y="3.5" width="13" height="9"/><path d="M1.5 3.5 8 9l6.5-5.5"/></svg>
        dmorrow@veltrowdrafts.com
      </li>
      <li>
        <svg viewBox="0 0 16 16" fill="#fff"><path d="M4.5 1.5c.6 0 1.6 2.4 1.6 3 0 .6-1 1-1 1.6 0 1 2.4 4.2 3.6 4.6.5.2 1-.8 1.6-.8s2.6 1.5 2.6 2.1c0 .8-1.3 2.3-2.4 2.3C6.6 14.3 2 8.3 2 4c0-1.2 1.5-2.5 2.5-2.5z"/></svg>
        000-000-0000
      </li>
      <li>
        <svg viewBox="0 0 16 16" fill="none" stroke="#fff" stroke-width="1.2"><circle cx="8" cy="8" r="6.5"/><ellipse cx="8" cy="8" rx="3" ry="6.5"/><path d="M1.5 8h13M2.5 4.8h11M2.5 11.2h11"/></svg>
        www.veltrowdrafts.com
      </li>
    </ul>

    <p class="address">Address Line, City, State, Zip Code</p>
  </section>

  <section class="card card--back">
    <div class="grid-fill" role="img" aria-label="Faint drafting grid background"></div>
    <svg class="frame" viewBox="0 0 497 283" aria-hidden="true">
      <g fill="none" stroke="var(--line-soft)" stroke-width="1.2">
        <rect x="45" y="25" width="407" height="233"/>
        <rect x="49" y="29" width="399" height="225"/>
      </g>
      <g fill="#000" stroke="var(--ink)" stroke-width="1.2">
        <rect x="42" y="22" width="10" height="10"/>
        <rect x="445" y="22" width="10" height="10"/>
        <rect x="42" y="251" width="10" height="10"/>
        <rect x="445" y="251" width="10" height="10"/>
      </g>
    </svg>
    <div class="brand-name"><span class="brand-mark"></span>Veltrow Drafts</div>
    <p class="website">www.veltrowdrafts.com</p>
  </section>

</body>
</html>
```